für ...Tracklist für Hip Hop Album Cover designen
Zielgruppe
Mein Name ist Jonas Rabeck, ich gehöre keiner Firma an. Ich habe ein Musikalbum produziert, dessen Cover noch eine geeignete Track(Song)list braucht.
Aufgabenstellung
Beachten Sie bitte, dass die Vorderseite (Junge mit Kind) und die Rückseite, was das Bild an sich betrifft, bereits fertig sind. Es geht einzig und allein um die Schrift der Tracks (Songs) ! Ich möchte, dass auf der Vorderseite unten links Welokori steht (wie auf Bild 1). In meiner Vorstellung möchte ich das in einem 'Bleistiftstil' haben, dem meine laienhaften Versuche (Bild 1) schon sehr nahe kamen. Auf der Rückseite Bild 2 möchte ich dass im selbigen Stil die Track(Song)list eingefügt wird. Diese habe ich beigefügt.
Ich bevorzuge dabei handgeschriebenes statt

```html
<!DOCTYPE html>
<html lang="de">
<head>
<meta charset="utf-8">
<title>Welokori – Albumcover und Tracklist</title>
<link href="https://fonts.googleapis.com/css2?family=Amatic+SC:wght@700&display=swap" rel="stylesheet">
<style>
  :root {
    --page: #ffffff;
    --brick-dark: #6e2e1e;
    --brick: #b2482c;
    --shutter-light: #c9d6d6;
    --shutter: #9fb0b0;
    --ramp: #4a4744;
    --ramp-red: #d3261e;
    --back-light: #ecebe6;
    --back-mid: #d6d4cd;
    --ink: #262626;
    --title-red: #e3262b;
  }
  * { margin: 0; padding: 0; box-sizing: border-box; }
  html, body { width: 1200px; height: 609px; overflow: hidden; background: var(--page); }
  .spread { position: relative; width: 1200px; height: 609px; }
  .panel { position: absolute; top: 9px; width: 592px; height: 592px; overflow: hidden; }
  .front { left: 5px; }
  .back { left: 603px; }
  .front-photo {
    position: absolute; inset: 0;
    background:
      linear-gradient(180deg, transparent 0 80%, var(--ramp) 80% 92%, var(--ramp-red) 92% 94.5%, #1c1b1a 94.5%),
      radial-gradient(ellipse 46% 52% at 42% 46%, var(--shutter-light), var(--shutter) 70%, transparent 72%),
      linear-gradient(135deg, var(--brick), var(--brick-dark));
  }
  .back-photo {
    position: absolute; inset: 0;
    background:
      repeating-linear-gradient(180deg, transparent 0 7px, rgba(0,0,0,0.06) 7px 8px),
      linear-gradient(180deg, var(--back-light), var(--back-mid));
  }
  .artist-name {
    position: absolute; left: 84px; top: 400px;
    font-family: "Amatic SC", "Comic Sans MS", cursive;
    font-weight: 700; font-size: 50px; letter-spacing: 1px;
    color: var(--title-red); text-transform: uppercase; line-height: 1;
  }
  .tracklist {
    position: absolute; left: 66px; top: 75px; list-style: none;
    font-family: "Amatic SC", "Comic Sans MS", cursive;
    font-weight: 700; font-size: 22px; color: var(--ink);
    text-transform: uppercase; line-height: 24.5px;
  }
  .track { display: flex; }
  .track-no { width: 23px; flex: none; }
</style>
</head>
<body>
<main class="spread">
  <section class="panel front">
    <div class="front-photo" role="img" aria-label="Foto: junger Mann mit verschränkten Armen und ein kleiner Junge vor einem hellen Rolltor in einem Ziegelbogen auf einer Laderampe"></div>
    <h1 class="artist-name">Welokori</h1>
  </section>
  <section class="panel back">
    <div class="back-photo" role="img" aria-label="Foto: verwittertes weißes Rolltor als Hintergrund"></div>
    <ol class="tracklist">
      <li class="track"><span class="track-no">1</span>Es schlägt 12</li>
      <li class="track"><span class="track-no">2</span>Wenn der Beat einsetzt</li>
      <li class="track"><span class="track-no">3</span>On Fire</li>
      <li class="track"><span class="track-no">4</span>Kein Bock</li>
      <li class="track"><span class="track-no">5</span>Judas feat Tannfeld</li>
      <li class="track"><span class="track-no">6</span>Ich bin Rapper</li>
      <li class="track"><span class="track-no">7</span>Hip Hop</li>
      <li class="track"><span class="track-no">8</span>Welokori</li>
      <li class="track"><span class="track-no">9</span>Kapitalismus</li>
      <li class="track"><span class="track-no">10</span>Verschwörungstheoretiker</li>
      <li class="track"><span class="track-no">11</span>Ich hasse es</li>
      <li class="track"><span class="track-no">12</span>Wo auch immer du spielst feat Lenni</li>
      <li class="track"><span class="track-no">13</span>Sportaholic</li>
      <li class="track"><span class="track-no">14</span>Sand am Meer</li>
      <li class="track"><span class="track-no">15</span>Erfahrungen</li>
      <li class="track"><span class="track-no">16</span>Entscheidungen feat Tannfeld</li>
      <li class="track"><span class="track-no">17</span>Ringelberg</li>
      <li class="track"><span class="track-no">18</span>Lebensabschnitt</li>
    </ol>
  </section>
</main>
</body>
</html>
```